Social Media Application Design - Android and IOS

I am ready to go live with new social media app however I am not comfortable with the current design. It is a not interactive or attractive enough. Please note the splash screen is a green, so preference would be to keep a green theme although I am more than happy to consider other colours that would improve the design.
The attachment has the app screens that need to be redesigned. They may not need massive changes , however keen to go live so looking for inspired designers to support with this project and many others that I have, including ongoing work on this app.
Target Market(s)
Millenials
Industry/Entity Type
Social
Colors
Designer to choose colors to be used in the design.
Requirements
Must have
- Please see attached document for screens that I would like redesigned. It needs to work with Android and IOS. I am looking for the design and not the functionality.
Nice to have
- Highly interactive design. Please see polling functionality of Loomrix.
Should not have
- should not be complicated - simplicity is the key

```html
<!DOCTYPE html>
<html lang="en">
<head>
<meta charset="utf-8">
<title>Post a Question – Screens</title>
<link href="https://fonts.googleapis.com/css2?family=Montserrat:wght@200;300;500;600;700&display=swap" rel="stylesheet">
<style>
  :root{
    --bg:#e4e6ea;
    --screen:#f6f7f7;
    --green:#1cc88a;
    --green-dark:#12b97c;
    --lime:#c9ee55;
    --ink:#3a3d42;
    --ink-light:#6e7177;
    --muted:#b9bcc0;
    --tint:#d6f3e6;
    --orange:#f07a3a;
    --salmon:#f0a48c;
    --dash:#c6c9cd;
    --white:#ffffff;
  }
  *{box-sizing:border-box;margin:0;padding:0}
  html,body{width:1200px;height:946px;overflow:hidden}
  body{background:var(--bg);font-family:"Montserrat",sans-serif;color:var(--ink)}
  .screens{display:flex;gap:45px;justify-content:center;padding-top:78px}
  .screen{width:340px;height:790px;background:var(--screen);border-radius:26px;overflow:hidden;
    box-shadow:0 24px 50px rgba(90,100,120,.18);display:flex;flex-direction:column}
  .app-bar{height:96px;background:linear-gradient(100deg,var(--green) 30%,var(--lime) 100%);
    display:flex;align-items:center;padding:0 22px;color:var(--white);position:relative}
  .app-bar svg{width:22px;height:22px}
  .app-bar h1{position:absolute;left:0;right:0;text-align:center;font-size:15px;font-weight:600;letter-spacing:.3px}
  .content{padding:30px 26px 0;flex:1;display:flex;flex-direction:column}
  .heading{font-size:27px;line-height:1.12;font-weight:200;color:var(--ink-light)}
  .heading strong{display:block;font-weight:700;color:var(--ink)}
  .topic-row{display:flex;justify-content:space-between;align-items:flex-start}
  .edit{display:flex;align-items:center;gap:6px;border:1.5px solid var(--orange);color:var(--orange);
    border-radius:20px;padding:5px 12px;font-size:12px;font-weight:500;margin-top:4px}
  .edit svg{width:12px;height:12px}
  .chips{display:flex;gap:10px;margin:18px 0 34px}
  .chip{background:var(--green);color:var(--white);border-radius:22px;padding:9px 17px;font-size:13px;font-weight:600;
    box-shadow:0 6px 12px rgba(28,200,138,.25)}
  .field{margin:14px 0 30px;border-bottom:1.5px solid var(--green);padding-bottom:8px;position:relative;display:flex;justify-content:space-between;align-items:flex-end}
  .field .placeholder{font-size:11px;color:var(--muted)}
  .field .limit{font-size:9px;color:var(--salmon);position:absolute;right:0;top:-16px}
  .field::after{content:"";position:absolute;right:0;bottom:-1px;border-left:8px solid transparent;border-bottom:8px solid var(--green)}
  .options-head{display:flex;justify-content:space-between;align-items:flex-end}
  .segmented{display:flex;background:var(--tint);border-radius:16px;font-size:11px;font-weight:500;color:#7fbf9f;margin-bottom:4px}
  .segmented span{padding:6px 9px;border-radius:16px}
  .segmented .active{background:var(--green);color:var(--white)}
  .option-grid{display:grid;grid-template-columns:1fr 1fr;gap:14px;margin-top:24px}
  .option{height:118px;border:1.5px dashed var(--dash);border-radius:10px;display:flex;flex-direction:column;
    align-items:center;justify-content:center;gap:7px;font-size:10px;font-weight:600;color:var(--ink)}
  .option svg{width:28px;height:28px}
  .option .hint{font-size:8px;font-weight:500}
  .post{margin:28px 0 0;height:52px;border-radius:28px;background:var(--green);color:var(--white);
    display:flex;align-items:center;justify-content:center;position:relative;font-weight:600;font-size:15px;
    box-shadow:0 10px 20px rgba(28,200,138,.3)}
  .post .send{position:absolute;right:16px;width:24px;height:24px;border-radius:50%;background:var(--white);
    display:flex;align-items:center;justify-content:center}
  .post .send svg{width:13px;height:13px}
</style>
</head>
<body>
<main class="screens">

  <!-- Audio options -->
  <section class="screen">
    <header class="app-bar">
      <svg viewBox="0 0 24 24" fill="none" stroke="currentColor" stroke-width="2.4" stroke-linecap="round"><path d="M20 12H5M11 6l-6 6 6 6"/></svg>
      <h1>Post a Question</h1>
    </header>
    <div class="content">
      <div class="topic-row">
        <h2 class="heading">Your question<strong>Is about</strong></h2>
        <span class="edit">Edit <svg viewBox="0 0 24 24" fill="none" stroke="currentColor" stroke-width="2.4"><path d="M15 4l5 5L9 20H4v-5z"/></svg></span>
      </div>
      <div class="chips"><span class="chip">Science</span><span class="chip">Health</span><span class="chip">Religion</span></div>
      <h2 class="heading">What is your<strong>Question?</strong></h2>
      <div class="field"><span class="placeholder">Type your question here...</span><span class="limit">30 words max</span></div>
      <div class="options-head">
        <h2 class="heading">What are the<strong>Options?</strong></h2>
        <div class="segmented"><span>Images</span><span>Text</span><span class="active">Audio</span></div>
      </div>
      <div class="option-grid">
        <div class="option">
          <svg viewBox="0 0 24 24" fill="none" stroke="var(--green)" stroke-width="2"><rect x="9" y="3" width="6" height="11" rx="3" fill="var(--green)"/><path d="M5 11a7 7 0 0014 0M12 18v3M9 21h6"/></svg>
          <span class="hint">1:30</span>Record Option 1
        </div>
        <div class="option">
          <svg viewBox="0 0 24 24" fill="none" stroke="var(--muted)" stroke-width="2"><rect x="9" y="3" width="6" height="11" rx="3"/><path d="M5 11a7 7 0 0014 0M12 18v3M9 21h6"/></svg>
          <span class="hint">Hold to Record</span>Record Option 2
        </div>
      </div>
      <div class="post">Post<span class="send"><svg viewBox="0 0 24 24" fill="var(--green)"><path d="M2 21l21-9L2 3v7l15 2-15 2z"/></svg></span></div>
    </div>
  </section>

  <!-- Image options -->
  <section class="screen">
    <header class="app-bar">
      <svg viewBox="0 0 24 24" fill="none" stroke="currentColor" stroke-width="2.4" stroke-linecap="round"><path d="M20 12H5M11 6l-6 6 6 6"/></svg>
      <h1>Post a Question</h1>
    </header>
    <div class="content">
      <div class="topic-row">
        <h2 class="heading">Your question<strong>Is about</strong></h2>
        <span class="edit">Edit <svg viewBox="0 0 24 24" fill="none" stroke="currentColor" stroke-width="2.4"><path d="M15 4l5 5L9 20H4v-5z"/></svg></span>
      </div>
      <div class="chips"><span class="chip">Science</span><span class="chip">Health</span><span class="chip">Religion</span></div>
      <h2 class="heading">What is your<strong>Question?</strong></h2>
      <div class="field"><span class="placeholder">Type your question here</span><span class="limit">30 words max</span></div>
      <div class="options-head">
        <h2 class="heading">What are the<strong>Options?</strong></h2>
        <div class="segmented"><span class="active">Images</span><span>Text</span><span>Audio</span></div>
      </div>
      <div class="option-grid">
        <div class="option">
          <svg viewBox="0 0 24 24" fill="none" stroke="var(--muted)" stroke-width="1.6"><path d="M3 8h4l2-3h6l2 3h4v11H3z"/><circle cx="12" cy="13" r="3.5"/></svg>
          Upload option 1
        </div>
        <div class="option">
          <svg viewBox="0 0 24 24" fill="none" stroke="var(--muted)" stroke-width="1.6"><path d="M3 8h4l2-3h6l2 3h4v11H3z"/><circle cx="12" cy="13" r="3.5"/></svg>
          Upload option 2
        </div>
      </div>
      <div class="post">Post<span class="send"><svg viewBox="0 0 24 24" fill="var(--green)"><path d="M2 21l21-9L2 3v7l15 2-15 2z"/></svg></span></div>
    </div>
  </section>

  <!-- Text options -->
  <section class="screen">
    <header class="app-bar">
      <svg viewBox="0 0 24 24" fill="none" stroke="currentColor" stroke-width="2.4" stroke-linecap="round"><path d="M20 12H5M11 6l-6 6 6 6"/></svg>
      <h1>Post a Question</h1>
    </header>
    <div class="content">
      <div class="topic-row">
        <h2 class="heading">Your question<strong>Is about</strong></h2>
        <span class="edit">Edit <svg viewBox="0 0 24 24" fill="none" stroke="currentColor" stroke-width="2.4"><path d="M15 4l5 5L9 20H4v-5z"/></svg></span>
      </div>
      <div class="chips"><span class="chip">Science</span><span class="chip">Health</span><span class="chip">Religion</span></div>
      <h2 class="heading">What is your<strong>Question?</strong></h2>
      <div class="field"><span class="placeholder">Type your question here...</span><span class="limit">30 words max</span></div>
      <div class="options-head">
        <h2 class="heading">What are the<strong>Options?</strong></h2>
        <div class="segmented"><span>Images</span><span class="active">Text</span><span>Audio</span></div>
      </div>
      <div class="option-grid">
        <div class="option">
          <svg viewBox="0 0 24 24" fill="none" stroke="var(--muted)" stroke-width="2" stroke-linecap="round"><path d="M4 7h16M4 12h12M4 17h16"/></svg>
          Type option 1
        </div>
        <div class="option">
          <svg viewBox="0 0 24 24" fill="none" stroke="var(--muted)" stroke-width="2" stroke-linecap="round"><path d="M4 7h16M4 12h12M4 17h16"/></svg>
          Type option 2
        </div>
      </div>
      <div class="post">Post<span class="send"><svg viewBox="0 0 24 24" fill="var(--green)"><path d="M2 21l21-9L2 3v7l15 2-15 2z"/></svg></span></div>
    </div>
  </section>

</main>
</body>
</html>
```